New Professional Business Web Site

We need a web design for an existing company based in Dallas called "FoxTrail".
We provide software and professional services to enterprise customers in the contact centre space. We have a global customer base but primarily US and UK.
Our initial products are as follows-
LineSight - an application that helps Vortiva contact centre managers and administrators observe individual calls in queue.
MassLoad - an application that allows Vortiva administrators to load large groups of extensions and associate them to places.
Clustra - an application that helps Vortiva customers manage multilayers of agent and place groups into hiearchical and geographical groups of groups.
We would like to see designs that use the colors black, gray, and red as this matches with our new logo we have had designed from this web site and will have available in a few days.
The final design should communicate professionalism, innovation, software, large corporation, and telecommunications.
We're looking to provide features like-
1) Interactive Support Portal for customers
2) Product Descriptions
3) Product Purchasing
4) Interactive Forum
Target Market(s)
enterprise companies interested in call center related products and services
Industry/Entity Type
Business

```html
<!DOCTYPE html>
<html lang="en">
<head>
<meta charset="utf-8">
<title>FoxTrail – Contact Centre Software</title>
<link rel="stylesheet" href="https://fonts.googleapis.com/css2?family=Arimo:ital,wght@0,400;0,700;1,700&family=Open+Sans:wght@400;600;700&family=Oswald:wght@600&display=swap">
<style>
:root{
  --red:#b3302a;
  --olive:#8c9a36;
  --olive-light:#b5c15a;
  --ink:#111;
  --text:#555;
  --grey-bg:#dcdcd2;
  --panel:#f4f4f4;
  --rule:#ccc;
  --white:#fff;
}
*{box-sizing:border-box;margin:0;padding:0}
html,body{width:1116px;height:1200px;overflow:hidden;background:var(--white)}
body{position:relative;font-family:"Arimo",Arial,sans-serif;color:var(--text)}
a{color:inherit;text-decoration:none}
.abs{position:absolute}

/* header */
.brand{left:24px;top:46px;display:flex;align-items:center;gap:14px}
.brand-mark{width:54px;height:54px;border-radius:50%;background:var(--red)}
.brand-name{font-family:"Open Sans",sans-serif;font-weight:700;font-size:46px;color:var(--ink);letter-spacing:-1px}
.util-links{right:58px;top:14px;font-family:"Open Sans",sans-serif;font-weight:700;font-size:13px;color:var(--ink);display:flex;gap:14px}
.util-links .register{color:var(--red)}
.main-nav{left:373px;top:55px;width:723px;height:57px;border-radius:14px;
  background:linear-gradient(#5a5a5a,#1c1c1c 45%,#111);
  display:flex;align-items:center;padding-left:44px;gap:15px;
  font-family:"Open Sans",sans-serif;font-size:15.5px;color:var(--white)}
.nav-shine{left:373px;top:112px;width:723px;height:30px;border-radius:0 0 14px 14px;
  background:linear-gradient(rgba(0,0,0,.08),rgba(255,255,255,0))}

/* hero */
.hero-bg{left:496px;top:144px;width:620px;height:532px;background:var(--grey-bg)}
.photo{background:linear-gradient(135deg,#e8e4df,#c9b8a6 45%,#8e7866)}
.photo-top{left:0;top:144px;width:496px;height:286px;background:linear-gradient(120deg,#dfe3e6,#e9d2c0 40%,#c7a88c 70%,#e8eaec)}
.photo-bottom{left:0;top:430px;width:498px;height:234px;background:linear-gradient(110deg,#b08a6e,#d9b79c 45%,#8c9ea8 80%,#dfe5ea)}
.hero-title{left:519px;top:176px;font-weight:700;font-style:italic;font-size:25px;color:#3a3a3a}
.hero-text{left:526px;top:220px;width:570px;font-size:14px;line-height:20px;color:#333}
.slide-dots{left:1035px;top:306px;display:flex;gap:5px}
.slide-dots span{width:11px;height:11px;background:var(--olive-light)}
.slide-dots span:first-child{background:var(--olive)}

.product-card{top:344px;width:293px;height:320px;color:var(--white)}
.product-card.line{left:513px;background:var(--red)}
.product-card.clu{left:807px;background:var(--olive)}
.card-title{position:absolute;left:24px;top:17px;font-family:"Oswald",sans-serif;font-weight:600;font-size:27px;letter-spacing:.3px}
.card-photo{position:absolute;left:24px;top:61px;width:245px;height:124px}
.line .card-photo{background:linear-gradient(100deg,#8d9aa3,#d7c3ae 50%,#eef0f1)}
.clu .card-photo{background:linear-gradient(100deg,#c8a78d,#e9ded2 50%,#3d3f44)}
.card-text{position:absolute;left:24px;top:203px;width:250px;font-size:14px;line-height:20px}
.clu .card-text{top:200px}
.card-btn{position:absolute;right:22px;bottom:0;width:77px;height:30px;background:var(--ink);
  font-weight:700;font-size:14px;display:flex;align-items:center;justify-content:center}

/* content */
.content{left:0;top:676px;width:1116px;height:424px;
  background:radial-gradient(ellipse at 50% 40%,#fff 55%,#e6e6e6)}
.col-rule{top:690px;width:2px;height:404px;background:linear-gradient(#fff,#ddd 30%,#ddd 70%,#fff)}
.section-title{font-family:"Open Sans",sans-serif;font-weight:700;font-size:17px;color:#222}
.section-title em{font-style:normal;color:var(--red)}
.news-item h3{font-size:14px;color:var(--red);font-weight:700;margin-bottom:12px}
.news-item p{font-size:14px;line-height:25.5px;color:#555}
.read-more{display:block;text-align:right;font-weight:700;font-size:14px;color:#555;margin-top:6px}
.news-divider{border:0;border-top:1px solid #999;margin:14px 0 14px}
.welcome p{font-size:14px;line-height:25.7px;color:#555;margin-bottom:25px}
.newsletter{left:780px;top:741px;width:303px;height:50px;border-radius:14px;background:#a4a4a4;
  display:flex;align-items:center;font-family:"Open Sans",sans-serif;font-size:14px;color:#e4e4e4}
.newsletter .field{flex:1;padding-left:20px;border-right:1px solid #ddd;height:22px;line-height:22px}
.newsletter .submit{padding:0 16px 0 12px;font-weight:700;color:var(--white)}
.testimonial{font-size:14px;line-height:25.5px;color:#555}
.author{text-align:right;font-family:"Open Sans",sans-serif;font-size:15px;color:#333}
.author b{color:var(--red)}
.view-all{width:77px;height:30px;background:var(--ink);color:var(--white);font-weight:700;font-size:14px;
  display:flex;align-items:center;justify-content:center}
.social{display:flex;gap:26px;font-family:"Open Sans",sans-serif;font-weight:700;font-size:15.5px;color:#555}
.social span{display:flex;align-items:center;gap:12px}
.social i{width:40px;height:40px;border-radius:50%;display:block}
.social .s1 i{background:#1e5c9a}
.social .s2 i{background:#58b4e6}

/* footer */
.footer{left:0;top:1098px;width:1116px;height:102px;background:var(--grey-bg);border-top:4px solid var(--ink);
  font-family:"Open Sans",sans-serif;font-size:15px;color:var(--ink);text-align:center}
.footer-nav{margin-top:30px;display:flex;justify-content:center;gap:17px}
.footer-nav .current{color:var(--red);text-decoration:underline}
.copyright{margin-top:6px}
.copyright em{font-style:normal;color:var(--red)}
</style>
</head>
<body>

<header>
  <a class="brand abs" href="#"><span class="brand-mark"></span><span class="brand-name">FoxTrail</span></a>
  <nav class="util-links abs"><a class="register" href="#">Register</a><span>|</span><a href="#">Sign In</a><span>|</span><a href="#">Help</a></nav>
  <nav class="main-nav abs">
    <a href="#">Home</a><span>|</span><a href="#">About Us</a><span>|</span><a href="#">IT Support</a><span>|</span><a href="#">Development</a><span>|</span><a href="#">Products</a><span>|</span><a href="#">Contact Us</a>
  </nav>
  <div class="nav-shine abs"></div>
</header>

<section class="hero">
  <div class="hero-bg abs"></div>
  <div class="photo-top abs" role="img" aria-label="Smiling support agent wearing a headset"></div>
  <div class="photo-bottom abs" role="img" aria-label="Close-up of a support agent speaking into a headset microphone"></div>
  <h1 class="hero-title abs">Interactive Support Portal for Customers</h1>
  <p class="hero-text abs">Lorem Ipsum is simply dummy text of the printing and typesetting industry. Lorem Ipsum has been the industry's standard dummy text ever since the 1500s, when an unknown printer took a</p>
  <div class="slide-dots abs"><span></span><span></span><span></span><span></span></div>

  <article class="product-card line abs">
    <h2 class="card-title">LINESIGHT</h2>
    <div class="card-photo" role="img" aria-label="Row of call centre agents with headsets"></div>
    <p class="card-text">Lorem Ipsum is simply dummy text of the printing and typesetting industry. Lorem Ipsum has been the industry's standard</p>
    <a class="card-btn" href="#">View</a>
  </article>
  <article class="product-card clu abs">
    <h2 class="card-title">CLUSTRA</h2>
    <div class="card-photo" role="img" aria-label="Agent with headset in front of a team of colleagues"></div>
    <p class="card-text">Lorem Ipsum is simply dummy text of the printing and typesetting industry. Lorem Ipsum has been the industry's standard</p>
    <a class="card-btn" href="#">View</a>
  </article>
</section>

<main>
  <div class="content abs"></div>
  <div class="col-rule abs" style="left:378px"></div>
  <div class="col-rule abs" style="left:746px"></div>

  <section class="abs" style="left:12px;top:705px;width:348px">
    <h2 class="section-title" style="margin-bottom:14px">LATEST <em>NEWS</em></h2>
    <div class="news-item">
      <h3>Lorem Ipsum</h3>
      <p>Lorem Ipsum is simply dummy text of the printing and typesetting industry. Lorem Ipsum has been the industry's standardLorem Ipsum is simply dummy text of the printing and typesetting industry.</p>
      <a class="read-more" href="#">Read More&gt;&gt;</a>
    </div>
    <hr class="news-divider">
    <div class="news-item">
      <h3>Lorem Ipsum</h3>
      <p>Lorem Ipsum is simply dummy text of the printing and typesetting industry. Lorem Ipsum has been the industry's standardLorem Ipsum is simply dummy text of the printing and typesetting industry.</p>
      <a class="read-more" href="#">Read More&gt;&gt;</a>
    </div>
  </section>

  <section class="welcome abs" style="left:402px;top:705px;width:320px">
    <h2 class="section-title" style="margin-bottom:14px">WELCOME TO <em>FOXTRAIL</em></h2>
    <div style="padding-left:11px">
      <p>Lorem Ipsum is simply dummy text of the printing and typesetting industry. Lorem Ipsum has been the industry's standardLorem Ipsum is simply dummy text of the printing and typesetting industry. Lorem Ipsum has been the industry's standardLorem Ipsum is simply dummy text of the printing and typesetting industry. Lorem Ipsum has been the industry's standard</p>
      <p>Lorem Ipsum is simply dummy text of the printing and typesetting industry. Lorem Ipsum has been the industry's standard</p>
    </div>
  </section>

  <section class="abs" style="left:771px;top:705px;width:330px">
    <h2 class="section-title">NEWS<em>LETTER</em></h2>
  </section>
  <form class="newsletter abs"><span class="field">Email</span><span class="submit">Submit &gt;&gt;</span></form>

  <section class="abs" style="left:771px;top:827px;width:322px">
    <h2 class="section-title" style="margin-bottom:12px">TEST<em>MONIALS</em></h2>
    <p class="testimonial" style="padding-left:7px">Lorem Ipsum is simply dummy text of the printing and typesetting industry.</p>
    <p class="author"><b>Dana</b>, USA</p>
    <a class="view-all" href="#" style="margin:8px 0 0 13px">View All</a>
    <h2 class="section-title" style="margin:22px 0 12px">FOLLOW US <em>ON</em></h2>
    <div class="social"><span class="s1"><i></i>Circlebook</span><span class="s2"><i></i>Chirpline</span></div>
  </section>
</main>

<footer class="footer abs">
  <nav class="footer-nav">
    <a class="current" href="#">Home</a><span>|</span><a href="#">About Us</a><span>|</span><a href="#">IT Support</a><span>|</span><a href="#">Development</a><span>|</span><a href="#">Products</a><span>|</span><a href="#">Contact Us</a>
  </nav>
  <p class="copyright">Copyright © 2011 <em>FoxTrail</em></p>
</footer>

</body>
</html>
```